Construction Company

Design a clutter free business card, it can be double-sided utilizing the logo for BDN Ltd simple with all relevant contact information.

Please also a letterhead design to function for the purposes of invoicing, all mail requirements, with header to be distinctive while the footer ties page together and incorporates all necessary information.

For now, please use generic / dummy text and when a winner is selected, I will disclose the contact information.

Hi Designers! Please read the updated brief which includes the design of a business card and letterhead. Thank you!

```html
<!DOCTYPE html>
<html lang="en">
<head>
<meta charset="utf-8">
<title>BDN Ltd Stationery</title>
<link rel="stylesheet" href="https://fonts.googleapis.com/css2?family=Lato:wght@400;700&family=Roboto:wght@400;500;700&display=swap">
<style>
:root{
  --navy:#07338f;
  --gold:#c29a24;
  --bg:#acaaab;
  --paper:#ffffff;
  --paper-soft:#f9f8fb;
  --ink:#333333;
  --stripe:#e3e6f0;
  --cream:#efe8d4;
  --silver:#c9c9cc;
}
*{box-sizing:border-box;margin:0;padding:0}
html,body{width:1200px;height:617px;overflow:hidden;background:var(--bg)}
body{position:relative;font-family:"Lato",sans-serif;color:var(--ink)}
.piece{position:absolute;overflow:hidden;box-shadow:1.5px 1.5px 2px rgba(0,0,0,.35)}
.wordmark{position:absolute;font-family:"Lato",sans-serif;font-weight:700;color:var(--navy);letter-spacing:.5px;white-space:nowrap;display:flex;align-items:center;gap:.25em}
.wordmark .dot{display:inline-block;width:.45em;height:.45em;border-radius:50%;background:var(--gold)}
.decor{position:absolute;border-radius:50%;background:var(--cream);opacity:.8}
.contacts{position:absolute;font-family:"Roboto",sans-serif;font-size:5px;letter-spacing:.4px;color:#222}
.contacts li{list-style:none;display:flex;align-items:center;gap:4px;height:8.2px}
.contacts svg{width:5px;height:5px;fill:none;stroke:var(--navy);stroke-width:1.2}
.band{position:absolute;left:0;right:0;background:var(--navy);color:#fff;font-family:"Roboto",sans-serif;font-size:4.4px;display:flex;align-items:center;gap:4px;padding-left:34px}
.band svg{width:5px;height:5px;fill:none;stroke:#fff;stroke-width:1.2}
.band .mark{position:absolute;width:6px;height:6px;border-radius:50%;background:var(--gold)}

/* business card front */
.card-front{left:88px;top:51px;width:247px;height:143px;background:var(--navy)}
.card-front .wordmark{color:var(--silver);font-size:38px;left:38px;top:46px}

/* business card back */
.card-back{left:88px;top:218px;width:247px;height:141px;background:var(--paper-soft)}
.card-back .wordmark{font-size:25px;left:14px;top:14px}
.card-back .decor{left:147px;top:24px;width:90px;height:90px}
.person-name{position:absolute;left:14px;top:64px;font-family:"Roboto",sans-serif;font-weight:700;font-size:8.5px;color:var(--navy)}
.person-role{position:absolute;left:14px;top:74px;font-family:"Roboto",sans-serif;font-size:5px;color:#222}
.card-back .contacts{left:14px;top:93px}
.card-back .band{top:119px;height:10.5px;padding-left:14px}
.card-back .band .mark{left:206px;top:2px}

/* envelope */
.envelope{left:24px;top:391px;width:342px;height:174px;background:linear-gradient(#ffffff 55%,#ececec)}
.envelope .wordmark{font-size:22px;left:24px;top:20px}
.envelope .contacts{left:24px;top:121px}
.envelope .band{top:149px;height:10px;width:147px;right:auto;padding-left:24px;clip-path:polygon(0 0,140px 0,147px 100%,0 100%)}
.address-window{position:absolute;left:191px;top:93px;width:126px;height:65px;border-radius:12px;background:linear-gradient(110deg,#0a3a9c 45%,#1a4aac 50%,#0a3a9c 62%);border:1.5px solid #0b3596}

/* letterhead */
.letterhead{left:394px;top:54px;width:363px;height:508px;background:var(--paper)}
.letterhead .wordmark{font-size:32px;left:33px;top:32px}
.headline{position:absolute;left:34px;top:104px;font-family:"Roboto",sans-serif;font-weight:400;font-size:19px;color:var(--navy)}
.headline-rule{position:absolute;left:34px;top:130px;width:68px;height:1.5px;background:var(--navy)}
.subhead{position:absolute;left:34px;top:139px;font-size:7px;color:#222}
.letter-body{position:absolute;left:34px;width:295px;font-size:6.9px;line-height:13.2px;text-align:justify;color:#333}
.letter-body.p1{top:155px}
.letter-body.p2{top:261px}
.closing{position:absolute;left:34px;top:367px;font-size:7px}
.signature{position:absolute;left:34px;top:384px;width:58px;height:20px;background:linear-gradient(90deg,rgba(7,51,143,.18),rgba(7,51,143,.06));border-radius:3px}
.signer{position:absolute;left:34px;top:409px;font-size:7.5px;line-height:10.5px;color:#333}
.letterhead .decor{left:207px;top:348px;width:120px;height:120px}
.letterhead .contacts{left:34px;top:451px}
.letterhead .band{top:482px;height:10px}
.letterhead .band .mark{left:307px;top:2px}

/* invoice */
.invoice{left:801px;top:57px;width:362px;height:508px;background:var(--paper-soft)}
.invoice .wordmark{font-size:32px;left:31px;top:29px}
.bill-to{position:absolute;left:33px;top:103px;font-family:"Roboto",sans-serif;font-size:5px;line-height:7.9px;color:#444;letter-spacing:-.1px}
.invoice-title{position:absolute;right:37px;top:97px;font-family:"Roboto",sans-serif;font-weight:700;font-size:19px;color:var(--navy);letter-spacing:.5px}
.invoice-meta{position:absolute;left:237px;width:88px;font-family:"Roboto",sans-serif;font-size:5.5px;color:#444;display:flex;justify-content:space-between}
.invoice-meta.num{top:120px}
.invoice-meta.date{top:134px}
.line-items{position:absolute;left:32px;top:156px;width:297px;height:229px;border:1px solid var(--navy);border-top:none}
.line-items .head{display:grid;grid-template-columns:32px 106px 58px 50px 1fr;height:16px;background:var(--navy);color:#fff;font-family:"Roboto",sans-serif;font-weight:700;font-size:7.5px;text-align:center;align-items:center}
.line-items .rows{position:absolute;left:0;right:0;top:16px;bottom:0;background:repeating-linear-gradient(var(--paper-soft) 0 16.3px,var(--stripe) 16.3px 32.6px)}
.line-items .col-rule{position:absolute;top:16px;bottom:0;width:1px;background:var(--navy)}
.payment-types{position:absolute;top:390px;left:0;font-family:"Roboto",sans-serif;font-size:5.5px;color:#333}
.payment-types span{position:absolute;white-space:nowrap}
.acceptance{position:absolute;left:35px;top:411px;font-family:"Roboto",sans-serif;font-size:5.3px;line-height:7px;color:#333}
.totals{position:absolute;left:228px;top:384px;width:101px;border:1px solid var(--navy);border-top:none;font-family:"Roboto",sans-serif;font-weight:700;font-size:7px;color:#222}
.totals div{display:grid;grid-template-columns:51px 1fr;height:16.5px;border-top:1px solid var(--navy)}
.totals span{display:flex;align-items:center;justify-content:center;border-right:1px solid var(--navy)}
.invoice .contacts{left:33px;top:453px}
.invoice .band{top:481px;height:10px;padding-left:33px}
.invoice .band .mark{left:306px;top:2px}
</style>
</head>
<body>

<!-- business card front -->
<section class="piece card-front">
  <div class="wordmark">BDN Ltd</div>
</section>

<!-- business card back -->
<section class="piece card-back">
  <div class="wordmark"><span class="dot"></span>BDN Ltd</div>
  <div class="decor" role="img" aria-label="Faint brand emblem decoration"></div>
  <div class="person-name">Marcus Hale</div>
  <div class="person-role">President</div>
  <ul class="contacts">
    <li><svg viewBox="0 0 10 10"><path d="M2 1l2 2-1 1.5a6 6 0 0 0 2.5 2.5L7 6l2 2-1.5 1.5C4.5 9 1 5.5.5 2.5z"/></svg>+00 000 000 000</li>
    <li><svg viewBox="0 0 10 10"><rect x="1" y="2" width="8" height="6"/><path d="M1 2l4 3.5L9 2"/></svg>info@bdnltd.com</li>
    <li><svg viewBox="0 0 10 10"><circle cx="5" cy="5" r="4"/><path d="M1 5h8M5 1c-2 2.5-2 5.5 0 8M5 1c2 2.5 2 5.5 0 8"/></svg>www.bdnltd.com</li>
  </ul>
  <div class="band"><svg viewBox="0 0 10 10"><path d="M5 9.5S1.5 6 1.5 4a3.5 3.5 0 0 1 7 0C8.5 6 5 9.5 5 9.5z"/><circle cx="5" cy="4" r="1.2"/></svg>00000 New York. unit 000 Torrance, CA 00000<span class="mark"></span></div>
</section>

<!-- envelope -->
<section class="piece envelope">
  <div class="wordmark"><span class="dot"></span>BDN Ltd</div>
  <ul class="contacts">
    <li><svg viewBox="0 0 10 10"><path d="M2 1l2 2-1 1.5a6 6 0 0 0 2.5 2.5L7 6l2 2-1.5 1.5C4.5 9 1 5.5.5 2.5z"/></svg>+00 000 000 000</li>
    <li><svg viewBox="0 0 10 10"><rect x="1" y="2" width="8" height="6"/><path d="M1 2l4 3.5L9 2"/></svg>info@bdnltd.com</li>
    <li><svg viewBox="0 0 10 10"><circle cx="5" cy="5" r="4"/><path d="M1 5h8M5 1c-2 2.5-2 5.5 0 8M5 1c2 2.5 2 5.5 0 8"/></svg>www.bdnltd.com</li>
  </ul>
  <div class="band"><svg viewBox="0 0 10 10"><path d="M5 9.5S1.5 6 1.5 4a3.5 3.5 0 0 1 7 0C8.5 6 5 9.5 5 9.5z"/><circle cx="5" cy="4" r="1.2"/></svg>00000 New York. unit 000 Torrance, CA 00000</div>
  <div class="address-window"></div>
</section>

<!-- letterhead -->
<section class="piece letterhead">
  <div class="wordmark"><span class="dot"></span>BDN Ltd</div>
  <h1 class="headline">HEADLINE</h1>
  <div class="headline-rule"></div>
  <p class="subhead">Lorem Ipsum Dolor Sit Amet</p>
  <p class="letter-body p1">Consectetur adipiscing elit. Duis eu semper turpis, non pulvinar mauris. Aenean et eros in justo pretium laoreet. Pellentesque pharetra purus dui, non vestibulum arcu dapibus at. Lorem ipsum dolor sit amet, consectetur adipiscing elit. Curabitur neque mauris, lobortis sed sem nec, iaculis hendrerit tellus. Pellentesque purus odio, ullamcorper non scelerisque nec, auctor et dui. In hac habitasse platea dictumst. Maecenas convallis ante sapien. In lacinia volutpat commodo. Mauris congue arcu non dui pretium volutpat. Quisque augue urna, pretium sed metus eget, mollis consectetur nunc. Donec laoreet turpis nec mi ultrices, at vulputate felis vestibulum.</p>
  <p class="letter-body p2">Integer blandit ut eros quis dictum. Pellentesque vel enim commodo, accumsan purus id, scelerisque metus. Donec volutpat lacinia enim in aliquet. Fusce t sagittis ultrices. Pellentesque ac est ornare, lobortis erat aliquet, malesuada turpis. Praesent non massa nec purus posuere vehicula ac ac felis. Nunc eleifend euismod orci. Phasellus quis faucibus erat.</p>
  <p class="closing">Sincerely,</p>
  <div class="signature" role="img" aria-label="Handwritten signature"></div>
  <p class="signer">Owen R Carter<br>Company Director</p>
  <div class="decor" role="img" aria-label="Faint brand emblem decoration"></div>
  <ul class="contacts">
    <li><svg viewBox="0 0 10 10"><path d="M2 1l2 2-1 1.5a6 6 0 0 0 2.5 2.5L7 6l2 2-1.5 1.5C4.5 9 1 5.5.5 2.5z"/></svg>+00 000 000 000</li>
    <li><svg viewBox="0 0 10 10"><rect x="1" y="2" width="8" height="6"/><path d="M1 2l4 3.5L9 2"/></svg>info@bdnltd.com</li>
    <li><svg viewBox="0 0 10 10"><circle cx="5" cy="5" r="4"/><path d="M1 5h8M5 1c-2 2.5-2 5.5 0 8M5 1c2 2.5 2 5.5 0 8"/></svg>www.bdnltd.com</li>
  </ul>
  <div class="band"><svg viewBox="0 0 10 10"><path d="M5 9.5S1.5 6 1.5 4a3.5 3.5 0 0 1 7 0C8.5 6 5 9.5 5 9.5z"/><circle cx="5" cy="4" r="1.2"/></svg>00000 New York. unit 000 Torrance, CA 00000<span class="mark"></span></div>
</section>

<!-- invoice -->
<section class="piece invoice">
  <div class="wordmark"><span class="dot"></span>BDN Ltd</div>
  <p class="bill-to">BILL TO :<br>LENA VARGA<br>1234 orem Street, Do or Sit Amet City<br>012-3456-7890<br>orem@psum.com</p>
  <h2 class="invoice-title">INVOICE</h2>
  <div class="invoice-meta num"><span>INVOICE#</span><span>45678</span></div>
  <div class="invoice-meta date"><span>DATE</span><span>10/10/2018</span></div>
  <div class="line-items">
    <div class="head"><span>No</span><span>DESCRIPTION</span><span>QTY</span><span>PRICE</span><span>AMOUNT</span></div>
    <div class="rows"></div>
    <div class="col-rule" style="left:31px"></div>
    <div class="col-rule" style="left:137px"></div>
    <div class="col-rule" style="left:195px"></div>
    <div class="col-rule" style="left:245px"></div>
  </div>
  <div class="payment-types">
    <span style="left:38px">VISA</span>
    <span style="left:72px">MC</span>
    <span style="left:107px">DEBIT</span>
    <span style="left:143px">CASH</span>
    <span style="left:182px">CHEQUE</span>
  </div>
  <p class="acceptance">Signature Indicates<br>Acceptance of Price &amp; term</p>
  <div class="totals">
    <div><span>SUB TOTAL</span></div>
    <div><span>GST#</span></div>
    <div><span>SUB TOTAL</span></div>
  </div>
  <ul class="contacts">
    <li><svg viewBox="0 0 10 10"><path d="M2 1l2 2-1 1.5a6 6 0 0 0 2.5 2.5L7 6l2 2-1.5 1.5C4.5 9 1 5.5.5 2.5z"/></svg>+00 000 000 000</li>
    <li><svg viewBox="0 0 10 10"><rect x="1" y="2" width="8" height="6"/><path d="M1 2l4 3.5L9 2"/></svg>info@bdnltd.com</li>
    <li><svg viewBox="0 0 10 10"><circle cx="5" cy="5" r="4"/><path d="M1 5h8M5 1c-2 2.5-2 5.5 0 8M5 1c2 2.5 2 5.5 0 8"/></svg>www.bdnltd.com</li>
  </ul>
  <div class="band"><svg viewBox="0 0 10 10"><path d="M5 9.5S1.5 6 1.5 4a3.5 3.5 0 0 1 7 0C8.5 6 5 9.5 5 9.5z"/><circle cx="5" cy="4" r="1.2"/></svg>00000 New York. unit 000 Torrance, CA 00000<span class="mark"></span></div>
</section>

</body>
</html>
```